3 out of 100 people will get deadly skin cancer - we need a great illustration that shows this!

We put together a prototype image that communicates lifetime skin cancer risk. (see attached). We are looking for illustrators who can take make a new/better/cooler graphic that communicates this idea. It could be as simple as a superior illustration of the graphic we have or illustrators can propose a completely different idea.What should the illustration communicate?U.S. adults have a lifetime risk of developing skin cancer of 1 in 5. But we don't want to show 1 in 5; we want to show that number in a larger group. For example, in the attached illustration we show 20 in 100 people get skin cancer (i.e., 100 beach towels/umbrellas and 20 of them are red). Research has shown that people are more likely to accurately understand numbers like this when you convey them for larger groups (i.e., 20 out of 100 rather than 1 out of 5). U.S. adults also have a lifetime risk of 2.3% of developing the deadliest form of skin cancer (melanoma). In other words, approximately 3 in 100 people will develop melanoma in their lifetime. Ideally, a single image will convey both lifetime skin cancer risk (20 in 100) and melanoma risk (3 in 100). We will award a top three as follows: 1st place = $300, 2nd place = $250, third place = $200. We will also buy any design beyond 3rd place that we like for $100. For example, we purchased 24 designs in our last contest on Artmarketly.This research is supported by funding from the Corvane Institute of Science.

Target Market(s)

The U.S. public; individuals at high risk of developing skin cancer

Industry/Entity Type

Medicine

Colors

Designer to choose colors to be used in the design.

Requirements
Must have
• an original illustration that conveys both lifetime risk of developing skin cancer (20 in 100) and melanoma (3 in 100).
Nice to have
• It can be beach towels and umbrellas, just like our prototype, or the designers can pitch an original idea. Imagery can be realistic or cartoonish (or something in between). It should be illustrations, though. Not edited photos. The image should be in color (no black and white illustrations).
Should not have
• Photos. Clip art. Free vector images.
• We are looking for original illustrations created by the designer.

```html
<!DOCTYPE html>
<html lang="en">
<head>
<meta charset="utf-8">
<title>3 in 100 – Lifetime Skin Cancer Risk</title>
<link rel="stylesheet" href="https://fonts.googleapis.com/css2?family=Montserrat:wght@800&display=swap">
<style>
  :root {
    --page: #ffffff;
    --panel: #e9eaec;
    --ink: #111111;
    --leaf-green: #68a843;
    --tube-teal: #5cc3c3;
    --leaf-red: #e5261d;
    --tube-orange: #f6a623;
    --leaf-black: #151515;
    --tube-pink: #f0858f;
  }
  html, body {
    margin: 0;
    width: 784px;
    height: 1200px;
    overflow: hidden;
    background: var(--page);
  }
  .poster {
    position: relative;
    width: 784px;
    height: 1200px;
  }
  .panel {
    position: absolute;
    left: 18px;
    top: 23px;
    width: 741px;
    height: 1143px;
    background: var(--panel);
  }
  .legend-item {
    position: absolute;
    top: 42px;
    width: 160px;
    margin-left: -80px;
    display: flex;
    flex-direction: column;
    align-items: center;
  }
  .legend-item.none { left: 143px; }
  .legend-item.care { left: 386px; }
  .legend-item.melanoma { left: 618px; }
  .legend-label {
    margin-top: 10px;
    font-family: "Montserrat", sans-serif;
    font-weight: 800;
    font-size: 15px;
    letter-spacing: 0.3px;
    color: var(--ink);
    white-space: nowrap;
  }
  .tube {
    width: 47px;
    height: 93px;
    border-radius: 4px 4px 20px 20px;
  }
  .tube.none {
    background: linear-gradient(180deg, var(--leaf-green) 0 44%, var(--tube-teal) 44% 100%);
  }
  .tube.care {
    background: linear-gradient(180deg, var(--leaf-red) 0 44%, var(--tube-orange) 44% 100%);
  }
  .tube.melanoma {
    background: linear-gradient(180deg, var(--leaf-black) 0 44%, var(--tube-pink) 44% 100%);
  }
  .risk-grid {
    position: absolute;
    left: 75px;
    top: 212px;
    display: grid;
    grid-template-columns: repeat(10, 47px);
    grid-auto-rows: 93px;
    column-gap: 17.6px;
    row-gap: 0.5px;
  }
</style>
</head>
<body>
<main class="poster">
  <div class="panel"></div>

  <div class="legend-item none">
    <div class="tube none" role="img" aria-label="Green leaf in a teal test tube"></div>
    <span class="legend-label">NO SKIN CARE</span>
  </div>
  <div class="legend-item care">
    <div class="tube care" role="img" aria-label="Red leaf in an orange test tube"></div>
    <span class="legend-label">SKIN CARE</span>
  </div>
  <div class="legend-item melanoma">
    <div class="tube melanoma" role="img" aria-label="Black leaf in a pink test tube"></div>
    <span class="legend-label">MELANOMA</span>
  </div>

  <section class="risk-grid" aria-label="100 people: 17 skin cancer, 3 melanoma">
    <!-- row 1 -->
    <div class="tube none" role="img" aria-label="No skin cancer"></div>
    <div class="tube none" role="img" aria-label="No skin cancer"></div>
    <div class="tube care" role="img" aria-label="Skin cancer"></div>
    <div class="tube none" role="img" aria-label="No skin cancer"></div>
    <div class="tube none" role="img" aria-label="No skin cancer"></div>
    <div class="tube none" role="img" aria-label="No skin cancer"></div>
    <div class="tube melanoma" role="img" aria-label="Melanoma"></div>
    <div class="tube none" role="img" aria-label="No skin cancer"></div>
    <div class="tube none" role="img" aria-label="No skin cancer"></div>
    <div class="tube none" role="img" aria-label="No skin cancer"></div>
    <!-- row 2 -->
    <div class="tube none" role="img" aria-label="No skin cancer"></div>
    <div class="tube none" role="img" aria-label="No skin cancer"></div>
    <div class="tube none" role="img" aria-label="No skin cancer"></div>
    <div class="tube none" role="img" aria-label="No skin cancer"></div>
    <div class="tube care" role="img" aria-label="Skin cancer"></div>
    <div class="tube none" role="img" aria-label="No skin cancer"></div>
    <div class="tube none" role="img" aria-label="No skin cancer"></div>
    <div class="tube none" role="img" aria-label="No skin cancer"></div>
    <div class="tube care" role="img" aria-label="Skin cancer"></div>
    <div class="tube none" role="img" aria-label="No skin cancer"></div>
    <!-- row 3 -->
    <div class="tube none" role="img" aria-label="No skin cancer"></div>
    <div class="tube none" role="img" aria-label="No skin cancer"></div>
    <div class="tube care" role="img" aria-label="Skin cancer"></div>
    <div class="tube none" role="img" aria-label="No skin cancer"></div>
    <div class="tube none" role="img" aria-label="No skin cancer"></div>
    <div class="tube none" role="img" aria-label="No skin cancer"></div>
    <div class="tube none" role="img" aria-label="No skin cancer"></div>
    <div class="tube none" role="img" aria-label="No skin cancer"></div>
    <div class="tube none" role="img" aria-label="No skin cancer"></div>
    <div class="tube care" role="img" aria-label="Skin cancer"></div>
    <!-- row 4 -->
    <div class="tube care" role="img" aria-label="Skin cancer"></div>
    <div class="tube none" role="img" aria-label="No skin cancer"></div>
    <div class="tube none" role="img" aria-label="No skin cancer"></div>
    <div class="tube none" role="img" aria-label="No skin cancer"></div>
    <div class="tube none" role="img" aria-label="No skin cancer"></div>
    <div class="tube care" role="img" aria-label="Skin cancer"></div>
    <div class="tube none" role="img" aria-label="No skin cancer"></div>
    <div class="tube none" role="img" aria-label="No skin cancer"></div>
    <div class="tube none" role="img" aria-label="No skin cancer"></div>
    <div class="tube none" role="img" aria-label="No skin cancer"></div>
    <!-- row 5 -->
    <div class="tube none" role="img" aria-label="No skin cancer"></div>
    <div class="tube none" role="img" aria-label="No skin cancer"></div>
    <div class="tube melanoma" role="img" aria-label="Melanoma"></div>
    <div class="tube none" role="img" aria-label="No skin cancer"></div>
    <div class="tube none" role="img" aria-label="No skin cancer"></div>
    <div class="tube none" role="img" aria-label="No skin cancer"></div>
    <div class="tube care" role="img" aria-label="Skin cancer"></div>
    <div class="tube none" role="img" aria-label="No skin cancer"></div>
    <div class="tube care" role="img" aria-label="Skin cancer"></div>
    <div class="tube none" role="img" aria-label="No skin cancer"></div>
    <!-- row 6 -->
    <div class="tube none" role="img" aria-label="No skin cancer"></div>
    <div class="tube none" role="img" aria-label="No skin cancer"></div>
    <div class="tube none" role="img" aria-label="No skin cancer"></div>
    <div class="tube care" role="img" aria-label="Skin cancer"></div>
    <div class="tube none" role="img" aria-label="No skin cancer"></div>
    <div class="tube none" role="img" aria-label="No skin cancer"></div>
    <div class="tube none" role="img" aria-label="No skin cancer"></div>
    <div class="tube none" role="img" aria-label="No skin cancer"></div>
    <div class="tube none" role="img" aria-label="No skin cancer"></div>
    <div class="tube none" role="img" aria-label="No skin cancer"></div>
    <!-- row 7 -->
    <div class="tube care" role="img" aria-label="Skin cancer"></div>
    <div class="tube none" role="img" aria-label="No skin cancer"></div>
    <div class="tube none" role="img" aria-label="No skin cancer"></div>
    <div class="tube none" role="img" aria-label="No skin cancer"></div>
    <div class="tube none" role="img" aria-label="No skin cancer"></div>
    <div class="tube none" role="img" aria-label="No skin cancer"></div>
    <div class="tube none" role="img" aria-label="No skin cancer"></div>
    <div class="tube melanoma" role="img" aria-label="Melanoma"></div>
    <div class="tube none" role="img" aria-label="No skin cancer"></div>
    <div class="tube none" role="img" aria-label="No skin cancer"></div>
    <!-- row 8 -->
    <div class="tube none" role="img" aria-label="No skin cancer"></div>
    <div class="tube none" role="img" aria-label="No skin cancer"></div>
    <div class="tube care" role="img" aria-label="Skin cancer"></div>
    <div class="tube none" role="img" aria-label="No skin cancer"></div>
    <div class="tube none" role="img" aria-label="No skin cancer"></div>
    <div class="tube none" role="img" aria-label="No skin cancer"></div>
    <div class="tube care" role="img" aria-label="Skin cancer"></div>
    <div class="tube none" role="img" aria-label="No skin cancer"></div>
    <div class="tube none" role="img" aria-label="No skin cancer"></div>
    <div class="tube none" role="img" aria-label="No skin cancer"></div>
    <!-- row 9 -->
    <div class="tube none" role="img" aria-label="No skin cancer"></div>
    <div class="tube none" role="img" aria-label="No skin cancer"></div>
    <div class="tube none" role="img" aria-label="No skin cancer"></div>
    <div class="tube care" role="img" aria-label="Skin cancer"></div>
    <div class="tube none" role="img" aria-label="No skin cancer"></div>
    <div class="tube none" role="img" aria-label="No skin cancer"></div>
    <div class="tube none" role="img" aria-label="No skin cancer"></div>
    <div class="tube none" role="img" aria-label="No skin cancer"></div>
    <div class="tube care" role="img" aria-label="Skin cancer"></div>
    <div class="tube none" role="img" aria-label="No skin cancer"></div>
    <!-- row 10 -->
    <div class="tube none" role="img" aria-label="No skin cancer"></div>
    <div class="tube care" role="img" aria-label="Skin cancer"></div>
    <div class="tube none" role="img" aria-label="No skin cancer"></div>
    <div class="tube none" role="img" aria-label="No skin cancer"></div>
    <div class="tube none" role="img" aria-label="No skin cancer"></div>
    <div class="tube care" role="img" aria-label="Skin cancer"></div>
    <div class="tube none" role="img" aria-label="No skin cancer"></div>
    <div class="tube none" role="img" aria-label="No skin cancer"></div>
    <div class="tube none" role="img" aria-label="No skin cancer"></div>
    <div class="tube none" role="img" aria-label="No skin cancer"></div>
  </section>
</main>
</body>
</html>
```